Website Design for Employee Moral and Happiness Company

Looking for a clean website design that explains our features in a step by step manner so our visitors know exactly what our site does before logging in.

The site is called "Velasto". See logo design and video for a sample of style and an overview of what we do.

Target Market(s)

Business owners that are looking to retain employees.

Number of Pages Required

1 page

```html
<!DOCTYPE html>
<html lang="en">
<head>
<meta charset="utf-8">
<title>Velasto – Employee Morale &amp; Happiness</title>
<link rel="stylesheet" href="https://fonts.googleapis.com/css2?family=Libre+Baskerville:wght@400;700&family=Poppins:wght@400;500;600;700&family=Roboto:wght@500;700&display=swap">
<style>
  :root{
    --orange:#f56600;
    --orange-deep:#e85d00;
    --navy:#2d3a5e;
    --navy-dark:#0f1f2e;
    --peach:#fdeadd;
    --peach-soft:#fff4ec;
    --beige:#ece4da;
    --ink:#161616;
    --white:#ffffff;
    --footer-bar:#121212;
  }
  *{margin:0;padding:0;box-sizing:border-box}
  html,body{width:1200px;height:3932px;overflow:hidden;background:var(--white)}
  body{position:relative;font-family:'Poppins',sans-serif;color:var(--ink)}
  .abs{position:absolute}
  .serif{font-family:'Libre Baskerville',serif;font-weight:700}
  .brand{font-family:'Libre Baskerville',serif;font-weight:700;color:var(--ink);letter-spacing:1px;white-space:nowrap}
  .btn{position:absolute;display:flex;align-items:center;justify-content:center;background:var(--orange);color:var(--white);font-family:'Poppins',sans-serif;font-weight:600;font-size:13px;letter-spacing:.5px;border-radius:3px;text-transform:uppercase;white-space:nowrap}
  .btn--dark{background:#050505}
  .placeholder{position:absolute}

  /* hero */
  .corner-blob{left:-84px;top:-84px;width:168px;height:168px;border-radius:50%;background:var(--peach)}
  .hero-blob{left:690px;top:-10px;width:590px;height:590px;border-radius:50%;background:var(--peach)}
  .hero-title{left:162px;top:188px;font-size:42px;line-height:54px;white-space:nowrap}
  .hero-art{left:606px;top:104px;width:516px;height:409px;border-radius:48% 48% 6px 6px;background:linear-gradient(135deg,#3aa8a8 0%,#2a5a86 50%,#0f1f2e 78%,#b6ada0 78%,#b6ada0 100%)}

  /* promo banner */
  .banner{left:162px;top:701px;width:876px;height:266px;border-radius:10px;background:linear-gradient(120deg,var(--orange) 60%,var(--orange-deep) 60%)}
  .banner-dots{left:957px;top:667px;width:106px;height:171px;background:rgba(200,200,200,.12)}
  .banner-art{left:198px;top:687px;width:239px;height:318px;border-radius:18px;background:linear-gradient(180deg,#f1e7dc,#e9ddd0);border:4px solid var(--navy)}
  .banner-kicker{left:504px;top:734px;font-size:25px;color:var(--white);white-space:nowrap}
  .banner-title{left:504px;top:764px;font-size:52px;font-weight:700;color:var(--white);line-height:60px;white-space:nowrap}
  .banner-sub{left:504px;top:820px;font-size:40px;color:var(--white);white-space:nowrap}

  /* retention */
  .wave{left:0;width:1200px}
  .ret-art{left:182px;top:1200px;width:475px;height:470px;border-radius:50%;background:radial-gradient(circle at 55% 45%,#2d3a5e 0%,#8ab5ae 32%,#fbe0cc 62%)}
  .ret-dots{left:160px;top:1172px;width:124px;height:148px;background:rgba(210,200,195,.2)}
  .ret-title{left:740px;top:1290px;font-size:56px;line-height:63px;white-space:nowrap}

  /* features */
  .section-title{left:0;width:1200px;text-align:center;font-size:44px;white-space:nowrap}
  .card{position:absolute;top:1947px;width:312px;height:168px;background:var(--white);border-radius:8px;box-shadow:0 4px 18px rgba(0,0,0,.08)}
  .card-icon{position:absolute;width:164px;height:164px;border-radius:50%;background:var(--navy);top:1865px;display:flex;align-items:center;justify-content:center}
  .card-icon .placeholder{position:static;width:84px;height:62px;border-radius:6px;background:var(--orange)}
  .card-label{position:absolute;top:2050px;width:312px;text-align:center;font-family:'Roboto',sans-serif;font-weight:700;font-size:30px}

  /* morale gallery */
  .frame{position:absolute;top:2665px;width:234px;height:300px;background:var(--white);box-shadow:0 6px 20px rgba(0,0,0,.1);padding:24px}
  .frame .placeholder{position:static;width:100%;height:100%;border:8px solid #eaeaea}
  .frame--a{left:206px;transform:rotate(-3deg)}
  .frame--b{left:475px;transform:rotate(1deg)}
  .frame--c{left:753px;transform:rotate(-2deg)}

  /* before / after */
  .polaroid{position:absolute;top:3195px;width:250px;height:355px;background:#e7ddd0;padding:16px 16px 60px}
  .polaroid .placeholder{position:static;width:100%;height:100%}
  .polaroid-caption{position:absolute;left:0;right:0;bottom:16px;text-align:center;font-family:'Libre Baskerville',serif;font-weight:700;font-size:22px}
  .polaroid--from{left:278px;transform:rotate(3deg)}
  .polaroid--to{left:658px;transform:rotate(-2deg)}
  .transition-art{left:530px;top:3280px;width:120px;height:270px;background:linear-gradient(180deg,rgba(245,102,0,.05),rgba(245,102,0,.14));border-radius:60px}

  /* footer */
  .footer{left:0;top:3608px;width:1200px;height:283px;background:var(--beige)}
  .contact{position:absolute;top:3755px;display:flex;gap:14px}
  .contact svg{flex:none}
  .contact h4{font-family:'Libre Baskerville',serif;font-size:14px;font-weight:700;margin-bottom:3px}
  .contact p{font-size:13px;line-height:21px;white-space:nowrap}
  .footer-bar{left:0;top:3891px;width:1200px;height:41px;background:var(--footer-bar);color:var(--white);font-size:13px}
  .footer-bar p{position:absolute;left:163px;top:11px}
  .social{position:absolute;top:14px;width:13px;height:13px;border-radius:50%;background:var(--white)}
</style>
</head>
<body>

<!-- Hero -->
<div class="abs corner-blob"></div>
<div class="abs hero-blob"></div>
<div class="abs brand" style="left:162px;top:10px;font-size:52px">Velasto</div>
<div class="btn" style="left:927px;top:23px;width:111px;height:37px;font-size:12px">Login</div>
<h1 class="abs serif hero-title">Start Building<br>Your Event<br>Today With Me!</h1>
<div class="btn" style="left:162px;top:383px;width:194px;height:43px">Contact us today!</div>
<div class="placeholder hero-art" role="img" aria-label="Illustration of a man working at a desk computer inside a large circular window"></div>

<!-- Promo banner -->
<div class="placeholder banner-dots" role="img" aria-label="Decorative dot pattern"></div>
<div class="abs banner"></div>
<div class="placeholder banner-art" role="img" aria-label="Illustration of two smartphones showing the Velasto app"></div>
<p class="abs serif banner-kicker">I am here</p>
<p class="abs banner-title">TO HELP</p>
<p class="abs serif banner-sub">Business Like Yours</p>
<div class="btn btn--dark" style="left:505px;top:893px;width:195px;height:43px">Contact us today!</div>

<!-- Retention -->
<svg class="abs wave" style="top:1085px" width="1200" height="600" viewBox="0 0 1200 600" aria-hidden="true">
  <defs>
    <linearGradient id="peachFadeA" x1="0" y1="0" x2="0" y2="1">
      <stop offset="0" stop-color="#fdeadd"/>
      <stop offset="1" stop-color="#ffffff"/>
    </linearGradient>
  </defs>
  <path d="M0 38 C150 0 300 10 450 35 C620 65 700 20 820 10 C980 -5 1080 50 1200 30 L1200 600 L0 600 Z" fill="url(#peachFadeA)"/>
</svg>
<div class="placeholder ret-dots" role="img" aria-label="Decorative dot pattern"></div>
<div class="placeholder ret-art" role="img" aria-label="Illustration of a smiling employee holding up an ID badge, framed inside a peach circle"></div>
<h2 class="abs serif ret-title">Increase<br>Employee<br>Retention</h2>
<div class="btn" style="left:742px;top:1505px;width:194px;height:43px">Contact us today!</div>

<!-- Features -->
<h2 class="abs serif section-title" style="top:1775px">From Raffles To Auctions</h2>
<div class="card" style="left:264px"></div>
<div class="card" style="left:624px"></div>
<div class="card-icon" style="left:338px"><div class="placeholder" role="img" aria-label="Illustration of a bid paddle"></div></div>
<div class="card-icon" style="left:698px"><div class="placeholder" role="img" aria-label="Illustration of a raffle ticket"></div></div>
<p class="card-label" style="left:264px">Auctions</p>
<p class="card-label" style="left:624px">Raffles</p>
<div class="btn" style="left:498px;top:2162px;width:195px;height:45px">Contact us today!</div>

<!-- Morale gallery -->
<svg class="abs wave" style="top:2255px" width="1200" height="560" viewBox="0 0 1200 560" aria-hidden="true">
  <defs>
    <linearGradient id="peachFadeB" x1="0" y1="0" x2="0" y2="1">
      <stop offset="0" stop-color="#fdeadd"/>
      <stop offset="1" stop-color="#ffffff"/>
    </linearGradient>
  </defs>
  <path d="M0 60 C160 20 300 40 420 55 C560 72 640 20 760 10 C900 0 1000 40 1200 15 L1200 560 L0 560 Z" fill="url(#peachFadeB)"/>
</svg>
<h2 class="abs serif section-title" style="top:2420px;line-height:52px">Boost Employee Morale<br>&amp; Transform Your Work Events</h2>

<svg class="abs" style="left:0;top:2570px" width="1200" height="120" viewBox="0 0 1200 120" aria-hidden="true">
  <g stroke="#1a1a1a" stroke-width="2" fill="none">
    <path d="M335 17 L228 110 M335 17 L418 105"/>
    <path d="M576 17 L505 105 M576 17 L682 105"/>
    <path d="M881 17 L775 110 M881 17 L955 105"/>
  </g>
  <g fill="#f56600">
    <circle cx="335" cy="15" r="8"/>
    <circle cx="576" cy="15" r="8"/>
    <circle cx="881" cy="15" r="8"/>
  </g>
</svg>
<div class="frame frame--a"><div class="placeholder" role="img" aria-label="Illustration of an employee looking at a smartphone" style="background:linear-gradient(160deg,#2d3a5e 55%,#6fa39a)"></div></div>
<div class="frame frame--b"><div class="placeholder" role="img" aria-label="Illustration of a woman holding a coffee cup" style="background:linear-gradient(160deg,#e9ddd0 30%,#e67c6c 60%,#6b2a3a)"></div></div>
<div class="frame frame--c"><div class="placeholder" role="img" aria-label="Illustration of three happy coworkers together" style="background:linear-gradient(160deg,#2d3a5e 35%,#e98d62 70%,#8ab5ae)"></div></div>

<!-- Before / after -->
<div class="abs brand" style="left:0;width:1200px;text-align:center;top:3090px;font-size:56px">Velasto</div>
<div class="polaroid polaroid--from">
  <div class="placeholder" role="img" aria-label="Illustration of a bored, yawning employee" style="background:linear-gradient(160deg,#2d3a5e 40%,#f08a3c 70%,#f6e39a)"></div>
  <p class="polaroid-caption">From this</p>
</div>
<div class="placeholder abs transition-art" role="img" aria-label="Decorative curly arrow leading from the bored employee to the happy team"></div>
<div class="polaroid polaroid--to">
  <div class="placeholder" role="img" aria-label="Illustration of three cheerful coworkers" style="background:linear-gradient(160deg,#2d3a5e 35%,#e98d62 70%,#8ab5ae)"></div>
  <p class="polaroid-caption">To this</p>
</div>

<!-- Footer -->
<footer>
  <div class="abs footer"></div>
  <div class="abs brand" style="left:0;width:1200px;text-align:center;top:3640px;font-size:62px">Velasto</div>

  <div class="contact" style="left:244px">
    <svg width="36" height="36" viewBox="0 0 36 36" aria-hidden="true"><g fill="none" stroke="#f56600" stroke-width="1.8"><path d="M18 33 C10 24 7 19 7 14 A11 11 0 0 1 29 14 C29 19 26 24 18 33 Z"/><circle cx="18" cy="14" r="4"/></g></svg>
    <div><h4>Address</h4><p>Consectetuer Adipiscing<br>Diam nonummy - 987 654</p></div>
  </div>
  <div class="contact" style="left:547px">
    <svg width="36" height="36" viewBox="0 0 36 36" aria-hidden="true"><path d="M9 5 L14 5 L16 12 L12 15 C14 20 17 23 22 25 L25 21 L32 23 L32 28 C32 30 30 32 28 32 C16 31 5 20 4 9 C4 7 6 5 9 5 Z" fill="none" stroke="#f56600" stroke-width="1.8" stroke-linejoin="round"/></svg>
    <div><h4>Phone</h4><p>+1 555 014 2276</p></div>
  </div>
  <div class="contact" style="left:780px">
    <svg width="36" height="36" viewBox="0 0 36 36" aria-hidden="true"><g fill="none" stroke="#f56600" stroke-width="1.8" stroke-linejoin="round"><path d="M4 14 L18 4 L32 14 L32 32 L4 32 Z"/><path d="M4 14 L18 24 L32 14"/></g></svg>
    <div><h4>Email</h4><p>info@velasto.com</p></div>
  </div>

  <div class="abs footer-bar">
    <p>Copyright © 2022 Velasto. All Rights Reserved.</p>
    <span class="social" style="left:934px"></span>
    <span class="social" style="left:978px"></span>
    <span class="social" style="left:1022px"></span>
  </div>
</footer>

</body>
</html>
```